"Tova's" Website Design

Tova's makes earth friendly, healthy, and delicious snacks that are completely gluten free. We are looking for a website that is easy to navigate, energetic, and conveys our purpose "To create healthy, earth-friendly, gluten free snacks that fill bellies and warm hearts."
Our first product is "Tova's Cheese Bursts" are a small, square, cracker pack with an unreasonable amount of cheddar cheese flavor. The flavor literally explodes in your mouth!
We really want our site to pop and show off some personality.
I'm attaching the logo for the company, feel free to go beyond the logo in terms of color.
Here are some sites that we like!
http://www.pollwinkle.example/company
http://www.brenmoor.example/
http://www.qx47.example/
http://www.teddyvales.example/
http://www.dunrise.example/food/products_zest/
http://www.marvelfrost.example/

```html
<!DOCTYPE html>
<html lang="en">
<head>
<meta charset="utf-8">
<title>Tova's</title>
<link rel="stylesheet" href="https://fonts.googleapis.com/css2?family=Josefin+Sans:wght@300;400&family=Open+Sans:wght@400&display=swap">
<style>
:root{
  --orange:#ff5a1f;
  --orange-deep:#e8470f;
  --orange-warm:#f26a1b;
  --header-top:#fdfdfd;
  --header-bottom:#e4e4e4;
  --panel:#ebebeb;
  --panel-edge:#dcdcdc;
  --text:#555;
  --nav-dark:#8a2e10;
  --button:#4a4a4a;
  --white:#fff;
}
*{margin:0;padding:0;box-sizing:border-box}
html,body{width:1075px;height:1200px;overflow:hidden}
body{position:relative;background:#f3f3f3;font-family:"Open Sans",Arial,sans-serif;color:var(--text)}
.abs{position:absolute}

.site-header{left:0;top:0;width:1075px;height:116px;background:linear-gradient(var(--header-top),var(--header-bottom))}
.brand{left:74px;top:14px;font-family:"Josefin Sans",Arial,sans-serif;font-weight:400;font-size:66px;color:var(--orange);line-height:1}
.search{left:588px;top:27px;width:225px;height:25px;border-radius:6px;background:#e9e9e9;border:1px solid #e2e2e2;font-size:11px;color:#777;padding:5px 10px}
.header-phone{left:833px;top:27px;font-family:"Josefin Sans",sans-serif;font-weight:300;font-size:22px;color:var(--white);opacity:.85}
.nav a{position:absolute;top:74px;font-family:"Josefin Sans",sans-serif;font-weight:300;font-size:21px;color:var(--orange-warm);text-decoration:none}
.nav a.current{color:var(--nav-dark)}

.hero-band{left:0;top:116px;width:1075px;height:387px;background:var(--orange-warm)}
.hero-photo{left:77px;top:116px;width:919px;height:387px;background:linear-gradient(120deg,#d8c390,#c9b27a 45%,#e2cf9d 75%,#bfa56c)}
.slide-arrow{top:289px;width:32px;height:32px}
.hero-marker{left:512px;top:479px;width:48px;height:48px;border-radius:50%;background:var(--orange);clip-path:inset(24px 0 0 0)}

.content-panel{left:107px;top:566px;width:859px;height:342px;background:var(--panel);border:1px solid var(--panel-edge)}
.tab{top:557px;height:32px;background:var(--orange);border:1px solid #d94a12;color:var(--white);font-family:"Josefin Sans",sans-serif;font-weight:300;font-size:21px;text-align:center;line-height:34px}
.card-photo{top:605px;width:249px;height:133px;border:5px solid var(--white);box-shadow:0 0 2px #ccc}
.card-text{top:748px;width:249px;font-size:10px;line-height:16.2px;text-align:justify}
.read-more{top:842px;width:87px;height:29px;background:var(--button);border:2px solid #bbb;color:#eee;font-size:11.5px;text-align:center;line-height:25px}

.site-footer{left:0;top:936px;width:1075px;height:264px;background:linear-gradient(var(--orange),var(--orange-deep))}
.footer-title{top:962px;font-family:"Josefin Sans",sans-serif;font-weight:300;font-size:20px;color:var(--white)}
.tweet{left:106px;top:1022px;width:151px;font-size:9px;line-height:16.2px;color:var(--white);text-align:justify}
.post-thumb{left:333px;width:54px;height:54px;border:2px solid #222}
.post-title{left:403px;font-size:14px;color:var(--white)}
.post-date{left:403px;font-size:11px;color:#c43d0b}
.map{left:556px;top:1004px;width:176px;height:180px;border:4px solid #222;background:linear-gradient(135deg,#dcd9c8,#b9cbe0 55%,#e6dfc5)}
.social{top:1004px;width:22px;height:22px;border-radius:3px;background:var(--white);opacity:.9}
.contact-icon{left:780px;width:25px;height:25px;border-radius:3px;background:#2a2a2a}
.contact-text{left:815px;font-size:14px;color:var(--white)}
</style>
</head>
<body>

<header class="abs site-header"></header>
<div class="abs brand">Tova's</div>
<div class="abs search">Search</div>
<div class="abs header-phone">(XXX) XXX XXXX</div>
<nav class="nav">
  <a class="current" style="left:518px">Home</a>
  <a style="left:643px">About us</a>
  <a style="left:784px">Products</a>
  <a style="left:927px">Contact</a>
</nav>

<section>
  <div class="abs hero-band"></div>
  <div class="abs hero-photo" role="img" aria-label="Close-up photo of cheesy filled snack rolls"></div>
  <svg class="abs slide-arrow" style="left:95px" viewBox="0 0 32 32"><circle cx="16" cy="16" r="16" fill="#333"/><path d="M19 9 L11 16 L19 23Z" fill="#e0a030"/></svg>
  <svg class="abs slide-arrow" style="left:944px" viewBox="0 0 32 32"><circle cx="16" cy="16" r="16" fill="#333"/><path d="M13 9 L21 16 L13 23Z" fill="#e0a030"/></svg>
  <div class="abs hero-marker"></div>
  <svg class="abs" style="left:529px;top:504px" width="14" height="8" viewBox="0 0 14 8"><path d="M0 8 L7 0 L14 8Z" fill="#fff" opacity=".8"/></svg>
</section>

<main>
  <div class="abs content-panel"></div>
  <div class="abs tab" style="left:161px;width:178px">WELCOME</div>
  <div class="abs tab" style="left:466px;width:140px">PRODUCTS</div>
  <div class="abs tab" style="left:744px;width:152px">BRANDS</div>

  <div class="abs card-photo" style="left:126px;background:linear-gradient(135deg,#8a5a2e,#d9c4a8 55%,#6a2a20)" role="img" aria-label="Photo of a cut stuffed cheese ball"></div>
  <div class="abs card-photo" style="left:411px;background:linear-gradient(135deg,#b07a2c,#e8d79a 55%,#a8b860)" role="img" aria-label="Photo of fried snacks with a pickle"></div>
  <div class="abs card-photo" style="left:696px;background:linear-gradient(135deg,#e06a18,#f2c48a 55%,#e8d8c0)" role="img" aria-label="Photo of a golden cheese bite"></div>

  <p class="abs card-text" style="left:127px">Lorem Ipsum is simply dummy text of the printing and typesetting industry. Lorem Ipsum has been the industry's standard dummy text ever since the 1500s, when an unknown printer took a galley of type and scrambled it to makebook.</p>
  <p class="abs card-text" style="left:412px">Lorem Ipsum is simply dummy text of the printing and typesetting industry. Lorem Ipsum has been the industry's standard dummy text ever since the 1500s, when an unknown printer took a galley of type and scrambled it to makebook.</p>
  <p class="abs card-text" style="left:696px">Lorem Ipsum is simply dummy text of the printing and typesetting industry. Lorem Ipsum has been the industry's standard dummy text ever since the 1500s, when an unknown printer took a galley of type and scrambled it to makebook.</p>

  <div class="abs read-more" style="left:129px">Read more</div>
  <div class="abs read-more" style="left:414px">Read more</div>
  <div class="abs read-more" style="left:699px">Read more</div>
</main>

<footer>
  <div class="abs site-footer"></div>
  <h3 class="abs footer-title" style="left:92px">Our Tweets</h3>
  <h3 class="abs footer-title" style="left:333px">Latest Posts</h3>
  <h3 class="abs footer-title" style="left:556px">Location</h3>
  <h3 class="abs footer-title" style="left:782px">Contact Us</h3>

  <p class="abs tweet">Lorem Ipsum is simply dummy text of the printing and typesetting industry. Lorem Ipsum has been the industry's standard dummy text ever since the 1500s...</p>

  <div class="abs post-thumb" style="top:1004px;background:linear-gradient(#6a4a2a,#c09050)" role="img" aria-label="Photo of a restaurant interior"></div>
  <div class="abs post-title" style="top:1000px">Lorem Lipsum</div>
  <div class="abs post-date" style="top:1019px">May 05, 2012</div>
  <div class="abs post-thumb" style="top:1068px;background:linear-gradient(#333,#888)" role="img" aria-label="Black and white photo"></div>
  <div class="abs post-title" style="top:1064px">Lorem Lipsum</div>
  <div class="abs post-date" style="top:1083px">May 05, 2012</div>
  <div class="abs post-thumb" style="top:1132px;background:linear-gradient(135deg,#1a3a6a,#c02a3a,#2a8a4a)" role="img" aria-label="Photo of colourful sweets"></div>
  <div class="abs post-title" style="top:1128px">Lorem Lipsum</div>
  <div class="abs post-date" style="top:1147px">May 05, 2012</div>

  <div class="abs map" role="img" aria-label="Street map showing the shop location"></div>

  <div class="abs social" style="left:782px"></div>
  <div class="abs social" style="left:817px"></div>
  <div class="abs social" style="left:852px"></div>
  <div class="abs social" style="left:887px"></div>
  <div class="abs social" style="left:922px"></div>

  <svg class="abs contact-icon" style="top:1042px" viewBox="0 0 25 25"><path d="M8 5 L11 9 L9 11 Q11 15 14 16 L16 14 L20 17 L18 20 Q10 20 6 8Z" fill="#fff"/></svg>
  <div class="abs contact-text" style="top:1045px">(XXX) XXX XXXX</div>
  <svg class="abs contact-icon" style="top:1073px" viewBox="0 0 25 25"><rect x="5" y="7" width="15" height="11" fill="#fff"/><path d="M5 7 L12.5 13 L20 7" stroke="#2a2a2a" stroke-width="1.5" fill="none"/></svg>
  <div class="abs contact-text" style="top:1076px">Email</div>
  <svg class="abs contact-icon" style="top:1103px" viewBox="0 0 25 25"><path d="M12.5 4 A6 6 0 0 1 18.5 10 Q18.5 14 12.5 21 Q6.5 14 6.5 10 A6 6 0 0 1 12.5 4Z" fill="#fff"/><circle cx="12.5" cy="10" r="2.2" fill="#2a2a2a"/></svg>
  <div class="abs contact-text" style="top:1106px">Address</div>
</footer>

</body>
</html>
```